I need a business card design for a new dance business. I offer classical Indian dance tuition and also professional performances. I want to offer the community a variety of Indian dance experiences which include: group class and private tuition, school and preschool educational courses and workshops. dance theatre performances, community function workshops and performances, Kids Bollywood parties, wedding & conference performances, mouth percussion classes, Indian mythology/ dance costume and make up workshops.
The final design should communicate a feeling and impression of the vibrance and energy of Indian dance.
Updates
Hi Everyone,
Project Deadline Extended
Reason: I would like to refine a few changes to the details of this lovely design and we have run out of time!
Project Deadline Extended
Reason: Still waiting to hear back form designer re two possible changes to the card design. Tomorrow is the deadline and I have sent several messages but with no response. I need to see this through before selecting this lovely design.
Thank you.
Tara
Industry/Entity Type
Preschool
Requirements
Must have
- The front of the business card should have the photo of me (my face and torso), surrounded entirely by a border of bright magenta (to match the magenta of my lipstick - it is the same as the magenta on my skirt in the second photo). Within the top border I want (perhaps yellow-gold) writing to say "Tara Holloway - Artistic Director" and within the bottom border it should read "Silver Creek Kathak Studio." If you turn the card on its side the left border should have my telephone number: 0417 826 394 and the right-hand border should read: silvercreekkathakstudio@fernmail.example
The reverse of the card should be the orange of the dance costume
and I'd like the picture of my feet and legs to be on the right side of the back of the card as a side border. Centre-aligned on the orange background it should read (perhaps in dark magenta):
Indian dance classes + private tuition
School + preschool educational courses and workshops
Dance theatre performances
Community function workshops and performances
Children's Bollywood parties
Wedding + conference performances
Mouth percussion classes
Indian mythology and dance demonstration workshops
Dance costume and make-up workshops
Nice to have
- A lovely artistic but easy-to-read font would be nice.

```html
<!DOCTYPE html>
<html lang="en">
<head>
<meta charset="utf-8">
<title>Silver Creek Kathak Studio – Card Reverse</title>
<link href="https://fonts.googleapis.com/css2?family=Crimson+Pro:wght@400&display=swap" rel="stylesheet">
<style>
  :root {
    --page: #ffffff;
    --costume-orange: #e0692a;
    --cream: #fbf1e6;
    --magenta: #a0186e;
    --magenta-deep: #6d0f4a;
    --gold: #d9a441;
    --umber: #5a2a18;
  }
  html, body {
    margin: 0;
    padding: 0;
    width: 1200px;
    height: 848px;
    overflow: hidden;
    background: var(--page);
  }
  .canvas {
    position: relative;
    width: 1200px;
    height: 848px;
  }
  .card-back {
    position: absolute;
    left: 414px;
    top: 118px;
    width: 374px;
    height: 612px;
    background: var(--costume-orange);
    overflow: hidden;
  }
  .side-photo {
    position: absolute;
    right: 0;
    top: 0;
    width: 196px;
    height: 100%;
    background:
      radial-gradient(ellipse 60px 90px at 120px 60px, rgba(90,42,24,0.85), rgba(90,42,24,0) 100%),
      radial-gradient(ellipse 90px 180px at 80px 220px, var(--magenta) 0%, rgba(160,24,110,0.9) 60%, rgba(160,24,110,0) 100%),
      radial-gradient(ellipse 40px 60px at 90px 380px, #c9455f 0%, rgba(201,69,95,0) 100%),
      radial-gradient(ellipse 50px 220px at 160px 380px, var(--gold) 0%, rgba(217,164,65,0) 100%),
      linear-gradient(90deg, rgba(224,105,42,1) 0%, rgba(224,105,42,0) 30%),
      linear-gradient(180deg, var(--umber) 0%, var(--magenta-deep) 20%, var(--magenta) 45%, #b8543a 70%, var(--gold) 85%, #a87a3a 100%);
  }
  .services {
    position: absolute;
    left: 12px;
    top: 76px;
    width: 160px;
    margin: 0;
    padding: 0;
    list-style: none;
    font-family: "Crimson Pro", Georgia, serif;
    font-size: 16px;
    line-height: 19px;
    color: var(--cream);
  }
  .services li {
    position: relative;
    padding-left: 18px;
    margin: 0;
  }
  .services li::before {
    content: "–";
    position: absolute;
    left: 0;
    top: 0;
  }
  .services .narrow { width: 110px; }
</style>
</head>
<body>
<div class="canvas">
  <section class="card-back">
    <div class="side-photo" role="img" aria-label="Photograph of a dancer's legs and hennaed foot with ankle bells, in a magenta and gold silk costume"></div>
    <ul class="services">
      <li class="narrow">Indian dance classes &amp; private tuition</li>
      <li class="narrow">School &amp; preschool educational courses and workshops</li>
      <li class="narrow">Dance theatre performances</li>
      <li>Community function workshops and performances</li>
      <li class="narrow">Children’s Bollywood parties</li>
      <li>Wedding &amp; conference performances</li>
      <li>Mouth percussion classes</li>
      <li>Indian mythology and dance demonstration workshops</li>
      <li>Dance costume and make-up workshops</li>
    </ul>
  </section>
</div>
</body>
</html>
```